Poster of Core Values & Motto

Create our core values poster and motto. Attached are our core values and our Motto. This poster represents both of our companies Tidy Pulp & CuraBinix.

Target Market(s)

Our team / employees

Industry/Entity Type

Shredding and Medical Waste

Colors
59FF00
82FF00
B8FF75
E3FFCB
F4FFEA
EB3D1F
EC4F4E
F09395
F8D3D4
FCEDEE

Requirements
Must have
• Include both companies logos

```html
<!DOCTYPE html>
<html lang="en">
<head>
<meta charset="utf-8">
<title>Core Values Poster – Tidy Pulp &amp; CuraBinix</title>
<link rel="stylesheet" href="https://fonts.googleapis.com/css2?family=Bebas+Neue&family=Montserrat:wght@400;500&family=Poppins:wght@500;700&display=swap">
<style>
  :root {
    --page-bg: #e4e4e4;
    --paper: #ffffff;
    --cura-red: #eb3d1f;
    --pulp-green: #1e9b3c;
    --ink: #1a1a1a;
    --band-light: #f08a6a;
    --band-main: #eb3d1f;
    --band-deep: #ee5a22;
    --on-band: #ffffff;
  }
  * { margin: 0; padding: 0; box-sizing: border-box; }
  html, body { width: 1200px; height: 888px; overflow: hidden; background: var(--page-bg); }
  .poster {
    position: absolute; left: 314px; top: 14px; width: 573px; height: 860px;
    background: var(--paper); overflow: hidden;
    font-family: "Montserrat", sans-serif;
  }
  .brand { position: absolute; left: 34px; }
  .brand-name { font-family: "Poppins", sans-serif; font-weight: 700; line-height: 1; }
  .brand-web { font-size: 12.5px; font-weight: 400; letter-spacing: 0.2px; }
  .brand-phone { font-family: "Poppins", sans-serif; font-weight: 700; font-size: 19px; letter-spacing: 0.5px; line-height: 1.2; }
  .brand--cura { top: 28px; color: var(--cura-red); }
  .brand--cura .brand-name { font-size: 22px; margin-bottom: 14px; letter-spacing: 0.5px; }
  .brand--pulp { top: 124px; color: var(--pulp-green); }
  .brand--pulp .brand-name { font-size: 19px; margin-bottom: 14px; display: flex; align-items: center; gap: 7px; }
  .brand-dot { width: 14px; height: 14px; border-radius: 50%; background: var(--pulp-green); }
  .divider { position: absolute; left: 277px; top: 28px; width: 1px; height: 47px; background: var(--ink); }
  .motto { position: absolute; left: 288px; top: 30px; color: var(--ink); }
  .motto-title { font-family: "Poppins", sans-serif; font-weight: 500; font-size: 20px; line-height: 1.1; letter-spacing: 0.2px; }
  .motto-line { font-family: "Poppins", sans-serif; font-weight: 500; font-size: 8.6px; margin-top: 3px; }
  .band {
    position: absolute; left: 0; top: 150px; width: 573px; height: 710px;
    background: linear-gradient(180deg, rgba(235,61,31,0) 0%, var(--band-light) 10%, var(--band-main) 20%, var(--band-main) 55%, var(--band-deep) 100%);
  }
  .headline {
    position: absolute; left: -197px; top: 519px; width: 552px; height: 100px;
    transform: rotate(-90deg); color: var(--on-band);
    font-family: "Bebas Neue", sans-serif; font-size: 142px; line-height: 108px;
    text-align: center; letter-spacing: 1px; white-space: nowrap;
  }
  .values { list-style: none; }
  .value { position: absolute; left: 278px; width: 280px; color: var(--on-band); }
  .value-icon { position: absolute; left: -73px; width: 56px; height: 56px; }
  .value-title { font-family: "Bebas Neue", sans-serif; font-size: 35px; line-height: 1; letter-spacing: 0.2px; }
  .value-text { font-size: 11.5px; line-height: 16px; letter-spacing: 0.6px; margin-top: 1px; }
</style>
</head>
<body>
<main class="poster">
  <div class="brand brand--cura">
    <div class="brand-name">CuraBinix</div>
    <div class="brand-web">WWW.CURABINIX.COM</div>
    <div class="brand-phone">844-555-0142</div>
  </div>
  <div class="brand brand--pulp">
    <div class="brand-name"><span class="brand-dot"></span>Tidy Pulp</div>
    <div class="brand-web">WWW.TIDYPULP.COM</div>
    <div class="brand-phone">1-844-PULP-000</div>
  </div>

  <div class="divider"></div>
  <div class="motto">
    <div class="motto-title">PURPOSE/CAUSE/PASSION</div>
    <div class="motto-line">REMIND PEOPLE WHAT GREAT SERVICE LOOKS LIKE</div>
  </div>

  <div class="band" role="img" aria-label="Snow-capped orange mountain range with a faded mountain photograph behind the values"></div>

  <div class="headline">CORE VALUES</div>

  <ul class="values">
    <li class="value" style="top:296px">
      <svg class="value-icon" style="top:-2px" viewBox="0 0 56 56" fill="none" stroke="#fff" stroke-width="3">
        <circle cx="28" cy="22" r="5" fill="#fff"/><path d="M19 36c0-6 4-9 9-9s9 3 9 9z" fill="#fff"/>
        <rect x="25" y="3" width="6" height="6" fill="#fff" stroke="none"/><rect x="25" y="47" width="6" height="6" fill="#fff" stroke="none"/>
        <circle cx="6" cy="28" r="3.5" fill="#fff" stroke="none"/><circle cx="50" cy="28" r="3.5" fill="#fff" stroke="none"/>
        <path d="M13 15l6-5M43 15l-6-5M13 41l6 5M43 41l-6 5"/>
      </svg>
      <div class="value-title">SYNERGY/ TEAMWORK</div>
      <div class="value-text">GET IT DONE ATTITUDE WITH HUMBLE CONFIDENCE</div>
    </li>
    <li class="value" style="top:386px">
      <svg class="value-icon" style="top:-2px" viewBox="0 0 56 56" fill="none" stroke="#fff" stroke-width="3">
        <circle cx="18" cy="18" r="12"/><path d="M16 13l3-2v14"/><path d="M11 29l-4 16 6-3 4 5 3-14"/>
        <path d="M30 50V32l6-10c2-3 5-1 4 2l-2 7h10c3 0 3 5 0 5h-1c2 0 2 4 0 4h-1c2 0 2 4-1 4H30z" fill="#fff"/>
        <rect x="49" y="32" width="5" height="18" fill="#fff" stroke="none"/>
      </svg>
      <div class="value-title">EXCELLENCE</div>
      <div class="value-text">EXCEED EXPECTATIONS WITH A SMILE</div>
    </li>
    <li class="value" style="top:475px">
      <svg class="value-icon" style="top:-2px" viewBox="0 0 56 56" fill="none" stroke="#fff" stroke-width="7">
        <path d="M12 48A22 22 0 1 1 44 48" stroke-dasharray="14 3"/>
        <path d="M20 22l10 14" stroke-width="5" stroke-linecap="round"/>
      </svg>
      <div class="value-title">EFFICIENT</div>
      <div class="value-text">ON-TIME, SENSE OF URGENCY, ALWAYS TRYING TO IMPROVE</div>
    </li>
    <li class="value" style="top:574px">
      <svg class="value-icon" style="top:0" viewBox="0 0 56 56">
        <path d="M28 3l20 7v16c0 13-9 22-20 27C17 48 8 39 8 26V10z" fill="#fff"/>
        <circle cx="28" cy="27" r="9" fill="none" stroke="#eb3d1f" stroke-width="3"/>
        <path d="M23 27l4 4 6-7" fill="none" stroke="#eb3d1f" stroke-width="3"/>
      </svg>
      <div class="value-title">SAFE &amp; SECURE</div>
      <div class="value-text">WE ARE JUST AS SECURE AS AN AS AN ARMORED TRUCK WITH MONEY</div>
    </li>
    <li class="value" style="top:684px">
      <svg class="value-icon" style="top:-2px" viewBox="0 0 56 56" fill="#fff">
        <rect x="4" y="4" width="20" height="10" rx="3"/><rect x="42" y="4" width="10" height="20" rx="3"/>
        <rect x="32" y="42" width="20" height="10" rx="3"/><rect x="4" y="32" width="10" height="20" rx="3"/>
        <path d="M28 16l12 12-12 12-12-12z"/>
      </svg>
      <div class="value-title">HONESTY/INTEGRITY</div>
      <div class="value-text">EXCEED EXPECTATIONS WITH A SMILE</div>
    </li>
    <li class="value" style="top:773px">
      <svg class="value-icon" style="top:0" viewBox="0 0 56 56" fill="#fff" stroke="#fff" stroke-width="3">
        <path d="M28 10L14 24l10 18 20-4zM14 24L6 40" fill="none"/>
        <circle cx="28" cy="10" r="7"/><circle cx="14" cy="24" r="5"/><circle cx="24" cy="42" r="5"/>
        <circle cx="44" cy="40" r="9"/><circle cx="6" cy="40" r="4"/>
      </svg>
      <div class="value-title">DEPENDABLE</div>
      <div class="value-text">ON-TIME, SENSE AS AN ARMORED TRUCK WITH MONEY</div>
    </li>
  </ul>
</main>
</body>
</html>
```